Business card design needed

We need a business card design for a new micro business based in Melbourne (Australia). Our main service is cleaning and fixing Vertical Blinds as a cheaper alternative than buying new blinds. A smaller part of the business is fitting affordable & temporary alternatives to double glazed windows both for noise abatement and climate control and reduction in energy costs.
We could be dealing with commercial as well as residential customers so we need a quality look. The design needs to reflect our core business of vertical blinds cleaning & maintenance.

Target Market(s)

Not sure yet. These Business Cards are going to be used to test the market

Industry/Entity Type

Residential

Contact Information for Business Card

Teloria Brinkhaus. Vertical Blinds Cleaning, Maintenance & Temporary Window Insulation Solutions. Ph: 03 9274 5163. Mob: 0497 362 514.

```html
<!DOCTYPE html>
<html lang="en">
<head>
<meta charset="utf-8">
<title>Teloria Brinkhaus – Business Card</title>
<link rel="stylesheet" href="https://fonts.googleapis.com/css2?family=Jost:wght@600&family=Oswald:wght@300&display=swap">
<style>
  :root {
    --backdrop: #ececec;
    --card: #ffffff;
    --accent: #e5771a;
    --ink: #1c1c1c;
    --on-accent: #ffffff;
  }
  html, body {
    margin: 0;
    width: 1200px;
    height: 800px;
    overflow: hidden;
    background: var(--backdrop);
  }
  .card {
    position: absolute;
    left: 40px;
    top: 85px;
    width: 1120px;
    height: 630px;
    background: var(--card);
  }
  .card__name {
    position: absolute;
    right: 65px;
    top: 90px;
    margin: 0;
    font: 600 42px/50px "Jost", sans-serif;
    color: var(--accent);
  }
  .card__tab {
    position: absolute;
    left: 203px;
    top: 229px;
    width: 88px;
    height: 173px;
    background: var(--accent);
  }
  .card__band {
    position: absolute;
    left: 311px;
    top: 229px;
    right: 0;
    height: 173px;
    background: var(--accent);
  }
  .card__services {
    position: absolute;
    left: 27px;
    top: 9px;
    margin: 0;
    font: 600 37px/54px "Jost", sans-serif;
    color: var(--on-accent);
    white-space: nowrap;
  }
  .card__contacts {
    position: absolute;
    left: 728px;
    top: 475px;
    margin: 0;
    padding: 0;
    list-style: none;
    font: 300 31px/56px "Oswald", sans-serif;
    color: var(--ink);
  }
  .contact {
    display: flex;
    align-items: center;
  }
  .contact__icon {
    width: 30px;
    height: 30px;
    margin-right: 7px;
    fill: var(--ink);
  }
</style>
</head>
<body>
  <main class="card">
    <h1 class="card__name">Teloria Brinkhaus</h1>
    <div class="card__tab"></div>
    <div class="card__band">
      <p class="card__services">Vertical Cleaning,<br>Maintenance and Temporary<br>Insulation Solutions for Windows.</p>
    </div>
    <ul class="card__contacts">
      <li class="contact">
        <svg class="contact__icon" viewBox="0 0 30 30" aria-label="Phone">
          <path d="M2 11c0-5 26-5 26 0v2h-7v-3c-3-1-9-1-12 0v3H2z"/>
          <path d="M8 13h14l5 11H3z"/>
          <circle cx="15" cy="19" r="3" fill="#fff"/>
        </svg>
        <span>: 03-9274-5163</span>
      </li>
      <li class="contact">
        <svg class="contact__icon" viewBox="0 0 30 30" aria-label="Mobile">
          <g transform="rotate(-30 15 15)">
            <rect x="9" y="3" width="12" height="25" rx="2"/>
            <rect x="11" y="6" width="8" height="7" fill="#fff"/>
            <rect x="17" y="-2" width="2" height="6"/>
          </g>
        </svg>
        <span>: 0497-362-514</span>
      </li>
    </ul>
  </main>
</body>
</html>
```